Health Promotion Charity Info-graphic of 2013 Activities

We need an Info-graphic which will be printed on A4 for distribution to our members, government, key stakeholders and grant providers. It will also be uploaded to our website - www.bright-sprouts.com.au

PROJECT BRIEF – Branding as per Bright Sprouts Association
The aim of this infographic is to show the work that Bright Sprouts Association did in 2013. It will be a pictorial annual report. It is to communicate to a wide audience the size and reach of Bright Sprouts Association activities.
We are a health promotion charity that supports schools to deliver healthy food services and our aim is to improve food literacy so kids know what to eat, when.... Our aim is to reduce diet related disease - mainly those relating to overweight and obesity. The infographic should be in keeping with our brand - see www.bright-sprouts.com.au

Using the following information
Our Members
In 2013 we had a total membership of 1,200
Our members are 1,137 Schools
20 Affiliates
24 Individuals
19 Leasees who operate 45 school canteens.
Our school members are
Public Sector Schools 846
Independent Schools 78
Catholic Schools 204
High schools 196
Primary 845
Central schools 30

There are 3082 schools in NSW – so we have 38% as members.

Our services
Supporting Schools
We answered 1078 enquiries through our telephone and email service.
We under took 20 menu assessments
22 school canteens had a business diagnostic
We flew to the regions and attended network meetings and school visits throughout New South Wales: South coast, Central Coast, north coast, illawarra, hunter new England and Dubbo

Publications
We produced the summer and winter editions of Bright Sprouts Tuckshop Digest magazine and
the Annual Bright Sprouts Tuckshop Digest Buyers Guide.

Food Industry
We work with the food industry to change the nutritional value of food
There were 57 food companies that registered 823 food products suitable for school canteens. Of these products, 359 were Green products and 464 amber products.

Community Activities
We worked with Riverbend and Hillcrest councils delivering 8 school holiday cooking classes to 80 children and their parents.

WEBSITE STATS – www.bright-sprouts.com.au
200,381 web visits
157,601 unique visitors
491.495 page views
2.45 pages per visitor

We worked with KORVO to develop the Tiffin Tin initiative which resulted in 79,289 Orbit and Pylon Downloads and
10,629 subscribers to the weekly KORVO email Tiffin Tin menu and shopping list.

Our funding
Total Income - $1,371,438
Government - $747,870 (54%)
Membership - $83,228 (6%)
Fee for Service – $42,946 (4%)
Other - $497,395(36%)
Total Equity $50,811

0555a3
9bcb3c
0593ce

```html
<!DOCTYPE html>
<html lang="en">
<head>
<meta charset="utf-8">
<title>Bright Sprouts – 2013 In Review</title>
<link href="https://fonts.googleapis.com/css2?family=Chewy&family=Open+Sans:wght@400;700&family=Montserrat:wght@800&family=Roboto+Slab:wght@400;700&display=swap" rel="stylesheet">
<style>
:root{
  --sky:#0aa5e4;
  --navy:#0555a3;
  --leaf:#5cb84a;
  --white:#ffffff;
  --hand:"Chewy", cursive;
  --body:"Open Sans", sans-serif;
  --stat:"Montserrat", sans-serif;
  --slab:"Roboto Slab", serif;
}
*{margin:0;padding:0;box-sizing:border-box}
html,body{width:849px;height:1200px;overflow:hidden;background:var(--white)}
.sheet{position:relative;width:849px;height:1200px;overflow:hidden;font-family:var(--body);color:var(--navy)}
.abs{position:absolute}
.header-wave{left:0;top:0}
.brand-badge{left:-8px;top:-6px;width:160px;height:160px;border-radius:50%;background:var(--white);display:flex;align-items:center;justify-content:center;text-align:center}
.brand-badge span{font-family:var(--hand);font-size:20px;line-height:1.05;color:var(--navy);width:110px}
.title{left:222px;top:30px;width:620px;font-family:var(--hand);font-size:82px;color:var(--white);letter-spacing:1px;line-height:1;white-space:nowrap;text-align:center}
.ribbon{left:0;top:168px}
.ribbon-text{left:47px;top:188px;font-family:var(--hand);font-size:40px;color:var(--white);line-height:1;white-space:nowrap}
h2{font-family:var(--hand);font-weight:400;font-size:27px;line-height:1;margin-bottom:2px;white-space:nowrap}
p{font-size:16.5px;line-height:17px}
b{font-weight:700}
.members{left:47px;top:288px;width:380px;color:var(--sky)}
.members h2{color:var(--navy)}
.members b{color:var(--navy)}
.members p+p{margin-top:17px}
.services{left:47px;top:624px;width:280px;color:var(--leaf)}
.services b{color:var(--navy)}
.card{left:451px;width:398px;color:var(--white);padding:18px 0 0 33px}
.card h2{font-size:27px}
.card p{width:340px}
.card-publications{top:287px;height:128px;background:var(--sky)}
.card-food{top:444px;height:181px;background:var(--leaf)}
.card-community{top:655px;height:148px;background:var(--sky);padding-top:24px}
.web-band{left:300px;top:840px;width:549px;height:145px;background:var(--leaf)}
.globe{left:283px;top:797px}
.web-head{left:449px;top:846px;color:var(--white)}
.web-head h2{font-size:28px}
.web-head .url{font-family:var(--slab);font-size:15px;margin-top:-2px}
.stat{color:var(--white);display:flex;align-items:center;gap:8px}
.stat svg{flex:none}
.stat strong{display:block;font-family:var(--stat);font-weight:800;font-size:16px;line-height:16px}
.stat span{font-family:var(--slab);font-size:15.5px;line-height:17px}
.tools-disc{left:-175px;top:845px;width:510px;height:510px;border-radius:50%;background:var(--navy)}
.tools-icon{left:46px;top:888px}
.tools-copy{left:47px;top:1018px;width:250px;color:var(--white);font-size:15.5px;line-height:22.6px}
.tools-copy b{font-weight:700}
.fund-band{left:500px;top:1035px;width:349px;height:155px;background:var(--sky)}
.fund-disc{left:321px;top:1008px;width:210px;height:210px;border-radius:50%;background:var(--sky);border:3px solid var(--white);box-shadow:0 0 0 8px var(--navy)}
.fund-dollar{left:395px;top:1020px;font-family:var(--hand);font-size:84px;color:var(--white);line-height:1}
.fund-label{left:380px;top:1118px;font-family:var(--hand);font-size:26px;color:var(--white);text-align:center;line-height:1.15}
.fund-list{left:563px;top:1054px;color:var(--white);font-family:var(--slab);font-size:16px;line-height:20.5px;list-style:none;white-space:nowrap}
.fund-list b{font-family:var(--stat);font-weight:800;font-size:15.5px}
</style>
</head>
<body>
<main class="sheet">
  <svg class="abs header-wave" width="849" height="290" viewBox="0 0 849 290" aria-hidden="true">
    <path d="M0 0H849V276C760 240 600 206 400 196C250 189 120 192 0 197Z" fill="#0555a3"/>
    <path d="M0 0H849V246C760 214 600 190 400 182C250 176 120 178 0 182Z" fill="#0aa5e4"/>
  </svg>
  <div class="abs brand-badge"><span>Bright Sprouts Association</span></div>
  <div class="abs title">Bright Sprouts</div>

  <svg class="abs ribbon" width="400" height="90" viewBox="0 0 400 90" aria-hidden="true">
    <polygon points="0,2 380,2 396,45 380,88 0,88" fill="#0555a3"/>
    <polyline points="0,8 374,8 389,45 374,82 0,82" fill="none" stroke="#fff" stroke-width="1.5" stroke-dasharray="5 4"/>
  </svg>
  <div class="abs ribbon-text">2013 In Review</div>

  <section class="abs members">
    <h2>Our Members</h2>
    <p>In 2013 we had a total membership of 1,200<br>
    <b>1,137</b> Schools Members<br>
    <b>20</b> Affiliates<br>
    <b>24</b> Individuals<br>
    <b>19</b> Leasees who operate 45 school canteens.</p>
    <p>Our school members are<br>
    <b>846</b> Public Sector Schools<br>
    <b>78</b> Independent Schools<br>
    <b>204</b> Catholic Schools<br>
    <b>196</b> High schools<br>
    <b>845</b> Primary<br>
    <b>30</b> Central schools</p>
    <p>There are 3082 schools in NSW –<br>so we have 38% as members.</p>
  </section>

  <section class="abs services">
    <h2>Our Services</h2>
    <p>Supporting Schools<br>
    We answered <b>1078</b> enquiries through our telephone and email service. We under took <b>20</b> menu assessments <b>22</b> school canteens had a business diagnostic. We flew to the regions and attended network meetings and school visits throughout New South Wales</p>
  </section>

  <section class="abs card card-publications">
    <h2>Publications</h2>
    <p>We produced the summer and winter editions of Bright Sprouts Tuckshop Digest magazine and the Annual Bright Sprouts Tuckshop Digest Buyers Guide.</p>
  </section>

  <section class="abs card card-food">
    <h2>Food Industry</h2>
    <p>We work with the food industry to change the nutritional value of food<br>
    There were <b>57</b> food companies that registered <b>823</b> food products suitable for school canteens. Of these products, <b>359</b> were Green products and <b>464</b> amber products.</p>
  </section>

  <section class="abs card card-community">
    <h2>Community Activities</h2>
    <p>We worked with Riverbend and Hillcrest councils delivering <b>8</b> school holiday cooking classes to <b>80</b> children and their parents.</p>
  </section>

  <div class="abs web-band"></div>
  <svg class="abs globe" width="150" height="150" viewBox="0 0 150 150" aria-hidden="true">
    <circle cx="75" cy="75" r="75" fill="#5cb84a"/>
    <circle cx="75" cy="75" r="60" fill="none" stroke="#fff" stroke-width="2" stroke-dasharray="3 3"/>
    <g fill="none" stroke="#fff" stroke-width="5">
      <circle cx="75" cy="75" r="30"/>
      <ellipse cx="75" cy="75" rx="13" ry="30"/>
      <line x1="45" y1="75" x2="105" y2="75"/>
      <path d="M50 60H100M50 90H100"/>
    </g>
  </svg>
  <div class="abs web-head">
    <h2>Website Stats</h2>
    <div class="url">www.bright-sprouts.com.au</div>
  </div>
  <div class="abs stat" style="left:452px;top:900px">
    <svg width="28" height="28" viewBox="0 0 28 28" aria-hidden="true"><circle cx="14" cy="14" r="13" fill="#fff"/><circle cx="14" cy="14" r="7" fill="none" stroke="#5cb84a" stroke-width="2.5"/><path d="M7 14h14" stroke="#5cb84a" stroke-width="2"/></svg>
    <div><strong>200,381</strong><span>web visits</span></div>
  </div>
  <div class="abs stat" style="left:452px;top:944px">
    <svg width="28" height="28" viewBox="0 0 28 28" aria-hidden="true"><circle cx="14" cy="14" r="13" fill="#fff"/><circle cx="14" cy="10" r="4" fill="#5cb84a"/><path d="M8 21a6 6 0 0 1 12 0z" fill="#5cb84a"/></svg>
    <div><strong>157,601</strong><span>unique visitors</span></div>
  </div>
  <div class="abs stat" style="left:616px;top:900px">
    <svg width="28" height="28" viewBox="0 0 28 28" aria-hidden="true"><circle cx="14" cy="14" r="12" fill="none" stroke="#fff" stroke-width="2.5"/><path d="M8.5 14.5l4 4 7-8" fill="none" stroke="#fff" stroke-width="2.5"/></svg>
    <div><strong>491.495</strong><span>page views</span></div>
  </div>
  <div class="abs stat" style="left:616px;top:944px">
    <svg width="28" height="28" viewBox="0 0 28 28" aria-hidden="true"><circle cx="14" cy="14" r="12" fill="none" stroke="#fff" stroke-width="2.5"/><circle cx="13" cy="13" r="4.5" fill="none" stroke="#fff" stroke-width="2.2"/><path d="M16.5 16.5l4 4" stroke="#fff" stroke-width="2.5"/></svg>
    <div><strong>2.45</strong><span>pages per visitor</span></div>
  </div>

  <div class="abs tools-disc"></div>
  <svg class="abs tools-icon" width="92" height="80" viewBox="0 0 92 80" aria-hidden="true">
    <g stroke="#fff" stroke-linecap="round" fill="none">
      <path d="M18 14L72 70" stroke-width="9"/>
      <path d="M78 6L22 66" stroke-width="7"/>
      <path d="M22 66L12 76" stroke-width="12"/>
    </g>
    <circle cx="16" cy="12" r="12" fill="#fff"/>
    <circle cx="10" cy="6" r="5" fill="#0555a3"/>
  </svg>
  <p class="abs tools-copy">We worked with KORVO to develop the Tiffin Tin initiative which resulted in <b>79,289</b> Orbit and Pylon Downloads and <b>10,629</b> subscribers to the weekly KORVO email Tiffin Tin menu and shopping list.</p>

  <div class="abs fund-band"></div>
  <div class="abs fund-disc"></div>
  <div class="abs fund-dollar">$</div>
  <div class="abs fund-label">Our<br>Funding</div>
  <ul class="abs fund-list">
    <li><b>$1,371,438</b> Total Income</li>
    <li><b>$747,870 (54%)</b> Government</li>
    <li><b>$83,228 (6%)</b> Membership</li>
    <li><b>$42,946 (4%)</b> Fee for Service</li>
    <li><b>$497,395(36%)</b> Other</li>
    <li><b>$50,811</b> Total Equity</li>
  </ul>
</main>
</body>
</html>
```